"Landing Page Design for Premium Eco-Friendly Laundry Strips – Plooifris.nl"

We need a visually appealing and high-converting landing page for our premium laundry strips, emphasizing luxury, sustainability, and ease of use. The page should include sections such as:

Hero Section: A compelling introduction with a strong headline, subheadline, and a clear call-to-action (CTA).
Product Benefits: Highlighting key features like eco-friendliness, long-lasting scent, and hypoallergenic qualities.
Product Description: Focusing on innovation and sustainability.
How It Works: Simple, visual steps for using the product.
Customer Reviews: Authentic testimonials to build trust and social proof.
FAQ Section: Addressing common concerns about the product.
The design should maintain a luxurious aesthetic while ensuring clarity and user-friendliness. We also offer free shipping on all orders, a key differentiator to be prominently displayed. All texts and translations are already provided for implementation. Please deliver the design in Figma format."

Target Market(s)

"Eco-conscious consumers and families seeking premium and sustainable laundry solutions. Target age group: 25-50, predominantly women who prioritize luxury and environmental impact."

Industry/Entity Type

"Laundry care and eco-friendly consumer goods."

Coding

Requirements
Must have
• A visually luxurious design emphasizing premium quality and eco-friendliness. Clear call-to-actions (e.g., 'Try Now – Free Shipping'). Sections for product benefits, how it works, customer reviews, and FAQ. Highlight free shipping with no minimum order prominently."
Nice to have
• Elegant, minimalist animations to enhance the premium feel. Subtle use of gold and black to emphasize luxury, with a touch of green for sustainability. Interactive customer reviews section (e.g., carousel or testimonials)."
Should not have
• Overly cluttered designs or overwhelming text blocks. Generic stock photos not aligned with our brand identity. Bright or overly playful color schemes that detract from the premium feel."

```html
<!DOCTYPE html>
<html lang="en">
<head>
<meta charset="utf-8">
<title>Plooifris.nl – Premium Eco-Friendly Laundry Strips</title>
<link rel="stylesheet" href="https://fonts.googleapis.com/css2?family=PT+Serif&family=Montserrat:wght@400;500;600;700&display=swap">
<style>
:root{
  --ink:#0c0b0f;
  --ink-soft:#141318;
  --panel:#1b1a20;
  --panel-line:#2a2830;
  --gold:#c68a2c;
  --gold-light:#e3ab45;
  --gold-deep:#9c6a1c;
  --cream:#f6deb4;
  --cream-light:#fbeed6;
  --beige:#ece0cc;
  --green:#6fae3a;
  --text:#f2efe9;
  --muted:#cfc9bf;
  --serif:"PT Serif", Georgia, serif;
  --sans:"Montserrat", Arial, sans-serif;
}
*{box-sizing:border-box;margin:0;padding:0}
html,body{width:1200px;height:4796px;overflow:hidden;background:var(--ink);color:var(--text);font-family:var(--sans)}
.page{position:relative;width:1200px;height:4796px;overflow:hidden;background:var(--ink)}
.abs{position:absolute}

/* shipping bar */
.ship-bar{left:0;top:0;width:1200px;height:37px;background:linear-gradient(90deg,#6b4a14,#b88428 30%,#d6a24a 50%,#b88428 70%,#6b4a14);display:flex;align-items:center;justify-content:center;gap:12px;font-size:15px;font-weight:600;color:#fff}
.ship-bar .truck{width:40px;height:28px;background:#2a1f0c;border-radius:4px;display:flex;align-items:center;justify-content:center}

/* header */
.hero-bg{left:0;top:37px;width:1200px;height:760px;background:radial-gradient(ellipse at 70% 40%,#26242b 0%,#15141a 55%,#0c0b0f 100%)}
.brand{left:138px;top:60px;width:130px;text-align:center}
.brand .dot{width:56px;height:56px;border:3px solid var(--gold);border-radius:50%;margin:0 auto 10px}
.brand .name{font-family:var(--serif);color:var(--gold);font-size:17px;letter-spacing:1px}
.nav{left:398px;top:88px;display:flex;gap:31px;font-family:var(--serif);font-size:14px;color:var(--text)}
.nav .active{color:var(--gold-light)}
.cart{left:1026px;top:84px;width:26px;height:26px;border-radius:50%;background:var(--gold-light);display:flex;align-items:center;justify-content:center}

/* hero */
.eyebrow{left:140px;top:268px;font-size:14px;font-weight:500;color:var(--green)}
.hero-title{left:140px;top:306px;width:420px;font-family:var(--serif);font-size:33px;line-height:39px;text-transform:uppercase;color:var(--text)}
.hero-title em{font-style:normal;color:var(--gold-light)}
.btn{display:inline-flex;align-items:center;justify-content:center;background:linear-gradient(180deg,var(--gold-light),var(--gold));color:#1a1206;font-weight:700;border-radius:22px;box-shadow:0 4px 10px rgba(0,0,0,.45)}
.hero-btn{left:140px;top:465px;width:268px;height:40px;font-size:16px}
.hero-photo{left:596px;top:212px;width:466px;height:466px;border-radius:50%;border:10px solid var(--gold);background:radial-gradient(circle at 60% 40%,#e8dccd,#b9a58c 55%,#6b5a48);overflow:hidden}
.hero-box{left:548px;top:436px;width:250px;height:224px;background:linear-gradient(135deg,#0f0f12 0%,#1f1c17 50%,#d9a445 51%,#f2ce7a 70%,#0f0f12 71%);border-radius:6px;box-shadow:0 10px 24px rgba(0,0,0,.6)}

/* benefits */
.benefits-shape{left:0;top:690px}
.section-kicker{width:1200px;left:0;text-align:center;font-size:30px;font-weight:500}
.section-title{width:1200px;left:0;text-align:center;font-family:var(--serif);font-size:50px;color:var(--gold);text-transform:uppercase;letter-spacing:.5px}
.benefits .section-kicker{color:#1d160c}
.benefits-box{left:504px;top:988px;width:212px;height:310px;background:linear-gradient(160deg,#101012 0%,#1a1814 55%,#d8a345 56%,#f3d07d 72%,#101012 73%);border-radius:4px;box-shadow:0 14px 28px rgba(80,50,10,.45)}
.pill{height:66px;border-radius:33px;background:linear-gradient(90deg,#efc98a,#f6d9a6);display:flex;align-items:center;gap:14px;padding:0 20px;font-size:16px;font-weight:500;color:#1d160c;line-height:19px}
.pill .ico{flex:none;width:36px;height:36px;border:2px solid #2a2014;border-radius:50%}
.pill-1{left:760px;top:954px;width:258px}
.pill-2{left:796px;top:1088px;width:266px}
.pill-3{left:770px;top:1243px;width:288px}

/* about */
.about-text{left:160px;top:1726px;width:880px;text-align:center;font-size:19px;line-height:29px;color:var(--text)}
.about-btn{left:465px;top:1877px;width:270px;height:40px;font-size:16px}

/* how it works */
.how-bg{left:0;top:2010px}
.step-circle{width:196px;height:196px;border-radius:50%;background:var(--beige);box-shadow:0 6px 18px rgba(0,0,0,.5)}
.step-num{width:58px;height:58px;border-radius:50%;background:var(--gold);color:var(--text);font-weight:700;font-size:28px;display:flex;align-items:center;justify-content:center}
.step-label{font-size:14px;line-height:24px;text-align:center;color:var(--text)}

/* reviews */
.card{background:var(--ink-soft);border:1px solid #1f1e24;border-radius:4px;padding:24px 24px}
.card .head{display:flex;align-items:center;gap:14px}
.avatar{width:46px;height:46px;border-radius:50%;background:var(--gold);display:flex;align-items:center;justify-content:center;font-weight:700;font-size:20px;color:#fff}
.card .who{font-size:16px;color:var(--gold);flex:1}
.card .q{font-family:var(--serif);font-size:40px;color:#4a4236;line-height:1}
.card p{margin-top:12px;font-size:13px;line-height:19px;color:var(--text)}
.card .verified{margin-top:16px;display:flex;align-items:center;gap:6px;font-size:11px;color:var(--muted)}
.card .verified i{width:10px;height:10px;background:#21b573;border-radius:50%;display:block}
.dots{left:505px;top:3486px;display:flex;gap:22px}
.dots span{width:20px;height:20px;border-radius:50%;background:var(--gold)}
.dots span.off{background:transparent;border:3px solid var(--gold)}

/* faq */
.faq{left:158px;top:3856px;width:884px}
.faq-item{background:var(--panel);margin-bottom:9px}
.faq-q{height:56px;display:flex;align-items:center;justify-content:space-between;padding:0 4px 0 28px;font-size:22px;color:var(--text)}
.faq-toggle{width:46px;height:46px;background:var(--gold);display:flex;align-items:center;justify-content:center}
.faq-a{padding:6px 28px 22px;font-size:11px;color:var(--text);background:var(--ink)}
.faq-item.open{background:var(--panel)}

/* footer */
.footer-brand{left:535px;top:4440px;width:130px;text-align:center}
.footer-brand .dot{width:66px;height:66px;border:3px solid var(--gold);border-radius:50%;margin:0 auto 12px}
.footer-brand .name{font-family:var(--serif);color:var(--gold);font-size:18px;letter-spacing:1px}
.footer-nav{left:0;width:1200px;top:4578px;display:flex;justify-content:center;gap:30px;font-family:var(--serif);font-size:14px;color:var(--text)}
.footer-nav .active{color:var(--gold-light)}
.socials{left:0;width:1200px;top:4637px;display:flex;justify-content:center;gap:17px}
.socials span{width:34px;height:34px;border-radius:50%;background:var(--gold-light);border:2px solid #8a5a12}
.footer-line{left:0;top:4724px;width:1200px;height:1px;background:#2a2830}
.copyright{left:0;width:1200px;top:4748px;text-align:center;font-size:12px;color:var(--text)}
.copyright em{font-style:normal;color:var(--gold)}
</style>
</head>
<body>
<main class="page">

  <!-- shipping bar -->
  <div class="abs ship-bar">
    <span class="truck"><svg width="26" height="18" viewBox="0 0 26 18"><rect x="1" y="2" width="15" height="10" fill="none" stroke="#fff" stroke-width="1.6"/><path d="M16 6h5l4 4v2h-9z" fill="none" stroke="#fff" stroke-width="1.6"/><circle cx="6" cy="14" r="2.5" fill="#fff"/><circle cx="20" cy="14" r="2.5" fill="#fff"/></svg></span>
    Free shipping with no minimum order
  </div>

  <!-- hero -->
  <section class="hero">
    <div class="abs hero-bg"></div>
    <div class="abs brand"><div class="dot"></div><div class="name">PLOOIFRIS</div></div>
    <nav class="abs nav">
      <span class="active">Home</span><span>About Us</span><span>Products</span><span>How it works</span><span>Testimonials</span><span>FAQ</span><span>Contact Us</span>
    </nav>
    <div class="abs cart"><svg width="14" height="14" viewBox="0 0 14 14"><path d="M1 2h2l2 7h6l2-5H4" fill="none" stroke="#fff" stroke-width="1.6"/><circle cx="6" cy="12" r="1.2" fill="#fff"/><circle cx="10.5" cy="12" r="1.2" fill="#fff"/></svg></div>

    <p class="abs eyebrow">Sustainable Freshness</p>
    <h1 class="abs hero-title">Premium <em>eco-friendly laundry strips</em> for a greener clean</h1>
    <a class="abs btn hero-btn">Free shipping on all orders</a>

    <div class="abs hero-photo" role="img" aria-label="Photo of a woman smelling fresh laundry in front of a washing machine"></div>
    <div class="abs hero-box" role="img" aria-label="Product photo of two black and gold laundry strip boxes"></div>
  </section>

  <!-- benefits -->
  <section class="benefits">
    <svg class="abs benefits-shape" width="1200" height="880" viewBox="0 0 1200 880" aria-hidden="true">
      <defs>
        <linearGradient id="benefitsFill" x1="0" x2="1" y1="0" y2="0">
          <stop offset="0" stop-color="#f0cf95"/><stop offset=".55" stop-color="#fbe9cc"/><stop offset="1" stop-color="#f4cf8e"/>
        </linearGradient>
      </defs>
      <path d="M0 17 Q600 130 1200 17 V855 Q600 740 0 855 Z" fill="url(#benefitsFill)"/>
      <path d="M0 17 Q600 130 1200 17" fill="none" stroke="var(--gold)" stroke-width="4"/>
      <path d="M0 855 Q600 740 1200 855" fill="none" stroke="var(--gold)" stroke-width="4"/>
    </svg>
    <svg class="abs" style="left:0;top:690px" width="560" height="880" viewBox="0 0 560 880" role="img" aria-label="Photo of a smiling woman holding a stack of folded towels in a wooden laundry room">
      <defs>
        <clipPath id="photoClip"><path d="M0 17 Q600 130 1200 17 V855 Q600 740 0 855 Z"/></clipPath>
        <linearGradient id="photoFill" x1="0" x2="1" y1="0" y2="1">
          <stop offset="0" stop-color="#c9925a"/><stop offset=".5" stop-color="#e6c39c"/><stop offset="1" stop-color="#b7a89a"/>
        </linearGradient>
      </defs>
      <rect x="0" y="0" width="560" height="880" fill="url(#photoFill)" clip-path="url(#photoClip)"/>
    </svg>

    <p class="abs section-kicker" style="top:836px">Our Product</p>
    <h2 class="abs section-title" style="top:880px">Benefits</h2>

    <svg class="abs" style="left:560px;top:950px" width="260" height="380" viewBox="0 0 260 380" aria-hidden="true">
      <path d="M20 12 Q180 20 200 170 Q200 300 120 330" fill="none" stroke="var(--gold)" stroke-width="2.5"/>
      <circle cx="172" cy="50" r="8" fill="#fbe9cc" stroke="var(--gold)" stroke-width="3"/>
      <circle cx="238" cy="172" r="8" fill="#fbe9cc" stroke="var(--gold)" stroke-width="3" transform="translate(-38 0)"/>
      <circle cx="196" cy="325" r="8" fill="#fbe9cc" stroke="var(--gold)" stroke-width="3" transform="translate(-42 -2)"/>
    </svg>
    <div class="abs benefits-box" role="img" aria-label="Product photo of a black and gold laundry strips box"></div>

    <div class="abs pill pill-1"><span class="ico"></span><span>Premium quality and<br>eco-friendliness</span></div>
    <div class="abs pill pill-2"><span class="ico"></span><span>Long-lasting scent</span></div>
    <div class="abs pill pill-3"><span class="ico"></span><span>Hypoallergenic qualities.</span></div>
  </section>

  <!-- about -->
  <section class="about">
    <p class="abs section-kicker" style="top:1598px">About</p>
    <h2 class="abs section-title" style="top:1642px">Product</h2>
    <p class="abs about-text">Premium eco-friendly laundry strips are a convenient, sustainable alternative to traditional laundry detergents. These strips are ultra-concentrated, pre-measured sheets that dissolve in water during the wash cycle, offering a lightweight, space-saving, and environmentally friendly option for laundry care.</p>
    <a class="abs btn about-btn">Try Now – Free Shipping</a>
  </section>

  <!-- how it works -->
  <section class="how">
    <svg class="abs how-bg" width="1200" height="860" viewBox="0 0 1200 860" role="img" aria-label="Dark background photo of a washing machine drum">
      <defs>
        <radialGradient id="drumFill" cx=".5" cy=".5" r=".7">
          <stop offset="0" stop-color="#2b2a30"/><stop offset=".6" stop-color="#1a191e"/><stop offset="1" stop-color="#0f0e12"/>
        </radialGradient>
      </defs>
      <path d="M0 0 Q600 140 1200 0 V845 Q600 760 0 845 Z" fill="url(#drumFill)"/>
      <path d="M0 0 Q600 140 1200 0" fill="none" stroke="var(--gold)" stroke-width="3"/>
      <path d="M0 845 Q600 760 1200 845" fill="none" stroke="var(--gold)" stroke-width="4"/>
    </svg>

    <p class="abs section-kicker" style="top:2134px;font-size:30px">Laundry Stripe</p>
    <h2 class="abs section-title" style="top:2180px">How it works</h2>

    <svg class="abs" style="left:150px;top:2290px" width="900" height="240" viewBox="0 0 900 240" aria-hidden="true">
      <path d="M40 10 Q180 -10 230 110 Q270 200 350 170 Q450 130 510 190 Q600 250 680 170 Q720 110 690 40" fill="none" stroke="var(--gold)" stroke-width="2" stroke-dasharray="6 6"/>
    </svg>

    <div class="abs step-circle" style="left:162px;top:2302px" role="img" aria-label="Illustration of a washing machine with laundry strips"></div>
    <div class="abs step-num" style="left:153px;top:2303px">01</div>
    <p class="abs step-label" style="left:130px;top:2514px;width:260px">Determine the amount of<br>detergent strips needed</p>

    <div class="abs step-circle" style="left:501px;top:2482px" role="img" aria-label="Illustration of a shirt being washed clean"></div>
    <div class="abs step-num" style="left:501px;top:2470px">02</div>
    <p class="abs step-label" style="left:470px;top:2404px;width:230px">Stains Removals and<br>colour Protected</p>

    <div class="abs step-circle" style="left:843px;top:2303px" role="img" aria-label="Illustration of a basket of fresh folded laundry"></div>
    <div class="abs step-num" style="left:828px;top:2314px">03</div>
    <p class="abs step-label" style="left:822px;top:2515px;width:240px">Sustainable Freshness</p>
  </section>

  <!-- testimonials -->
  <section class="reviews">
    <p class="abs section-kicker" style="top:2897px">Reviews</p>
    <h2 class="abs section-title" style="top:2950px">Testimonials</h2>

    <article class="abs card" style="left:71px;top:3078px;width:334px;height:272px">
      <div class="head"><span class="avatar">LV</span><span class="who">Lotte Van Dijk</span><span class="q">“”</span></div>
      <p>"You smell so good!"<br>Every day people ask me what detergent I use... your clothes smell so nice... well, then I send them to Plooifris! Tip, run your normal wash program and when it's done, run the rinse program with a large cap of laundry perfume.</p>
      <div class="verified"><i></i>Verified review</div>
    </article>
    <article class="abs card" style="left:432px;top:3116px;width:334px;height:262px">
      <div class="head"><span class="avatar">MJ</span><span class="who">Mira Jansen</span><span class="q">“”</span></div>
      <p>The most delicious fragrance experience<br>Lovely scent for my detergent. When I hang the laundry the whole house smells so nice. The scent also lingers well in the dryer. Super happy with it. Favorite is Amber Bloom</p>
      <div class="verified"><i></i>Verified review</div>
    </article>
    <article class="abs card" style="left:794px;top:3078px;width:334px;height:272px">
      <div class="head"><span class="avatar">LV</span><span class="who">Lotte Van Dijk</span><span class="q">“”</span></div>
      <p>"You smell so good!"<br>Every day people ask me what detergent I use... your clothes smell so nice... well, then I send them to Plooifris! Tip, run your normal wash program and when it's done, run the rinse program with a large cap of laundry perfume.</p>
      <div class="verified"><i></i>Verified review</div>
    </article>

    <div class="abs dots"><span></span><span class="off"></span><span></span><span></span><span></span></div>
  </section>

  <!-- faq -->
  <section class="faq-section">
    <svg class="abs" style="left:0;top:3560px" width="1200" height="90" viewBox="0 0 1200 90" aria-hidden="true">
      <path d="M0 4 Q600 150 1200 4" fill="none" stroke="var(--gold)" stroke-width="3"/>
    </svg>
    <p class="abs section-kicker" style="top:3700px">FAQ</p>
    <h2 class="abs section-title" style="top:3752px">Frequently asked question</h2>

    <div class="abs faq">
      <div class="faq-item open">
        <div class="faq-q">Are our laundry stripes vegan?<span class="faq-toggle"><svg width="22" height="22" viewBox="0 0 22 22"><path d="M3 11h16" stroke="#fff" stroke-width="2"/></svg></span></div>
        <p class="faq-a">Absolutely, all our laundry perfumes are vegan. They do not contain any animal products or by-products, in line with our ethical values.</p>
      </div>
      <div class="faq-item"><div class="faq-q">Are our laundry stripes suitable for all types of textiles?<span class="faq-toggle"><svg width="22" height="22" viewBox="0 0 22 22"><path d="M3 11h16M11 3v16" stroke="#fff" stroke-width="2"/></svg></span></div></div>
      <div class="faq-item"><div class="faq-q">Can our laundry stripes be used in combination with fabric softener?<span class="faq-toggle"><svg width="22" height="22" viewBox="0 0 22 22"><path d="M3 11h16M11 3v16" stroke="#fff" stroke-width="2"/></svg></span></div></div>
      <div class="faq-item"><div class="faq-q">Where can I buy our laundry stripes?<span class="faq-toggle"><svg width="22" height="22" viewBox="0 0 22 22"><path d="M3 11h16M11 3v16" stroke="#fff" stroke-width="2"/></svg></span></div></div>
      <div class="faq-item"><div class="faq-q">How much laundry stripes should I use per wash?<span class="faq-toggle"><svg width="22" height="22" viewBox="0 0 22 22"><path d="M3 11h16M11 3v16" stroke="#fff" stroke-width="2"/></svg></span></div></div>
    </div>
  </section>

  <!-- footer -->
  <footer class="footer">
    <svg class="abs" style="left:0;top:4362px" width="1200" height="70" viewBox="0 0 1200 70" aria-hidden="true">
      <path d="M0 60 Q600 -40 1200 60" fill="none" stroke="var(--gold)" stroke-width="4"/>
    </svg>
    <div class="abs footer-brand"><div class="dot"></div><div class="name">PLOOIFRIS</div></div>
    <nav class="abs footer-nav">
      <span class="active">Home</span><span>About Us</span><span>Products</span><span>How it works</span><span>Testimonials</span><span>FAQ</span><span>Contact Us</span>
    </nav>
    <div class="abs socials"><span></span><span></span><span></span><span></span></div>
    <div class="abs footer-line"></div>
    <p class="abs copyright"><em>© 2024 .</em> www.plooifris.com</p>
  </footer>

</main>
</body>
</html>
```